School ad poster design for athletic center

We need a banner designed which will hang in a local fitness center. It will hang in the indoor track so it should be simple, bold and easy to read. We are advertising our school: The Linden School at Marwick. I'd like to include one \ some of the photos attached. It should also be within our brand guidelines. Banner should be sent in a 4-color high resolution PDF, the size is 8’ X 3’, we will print it out here on premium quality vinyl poster material. I would like the name of the school and a version of the following message "A caring community where students with complex learning challenges love to learn"

Target Market(s)

Parents of students with learning disabilities

Industry/Entity Type

Education

Font styles to use
Other font styles liked:
• See style guide

Requirements
Must have
• Logo and be in brand. Clean design - easy to read
Nice to have
• If you can work the yoga picture in that would be nice.

```html
<!DOCTYPE html>
<html lang="en">
<head>
<meta charset="utf-8">
<title>The Linden School at Marwick – Fitness Center Banner</title>
<link rel="stylesheet" href="https://fonts.googleapis.com/css2?family=Lora:wght@400;500&display=swap">
<style>
  :root {
    --page-bg: #f4f4f4;
    --banner-bg: #ffffff;
    --navy: #1e3249;
    --photo-classroom: #6f8fb3;
    --photo-classroom-2: #c9a98a;
    --photo-portrait: #3a3f4a;
    --photo-portrait-2: #b9b3ad;
    --photo-yoga: #b98a6c;
    --photo-yoga-2: #7fb0c4;
    --photo-family: #5b6a72;
    --photo-family-2: #d9d4cf;
  }
  * { box-sizing: border-box; margin: 0; padding: 0; }
  html, body {
    width: 1200px;
    height: 1200px;
    overflow: hidden;
    background: var(--page-bg);
  }
  .banner {
    position: absolute;
    left: 40px;
    top: 374px;
    width: 1122px;
    height: 422px;
    background: var(--banner-bg);
    box-shadow: 0 1px 4px rgba(0,0,0,0.12);
  }
  .banner-header {
    position: relative;
    height: 194px;
  }
  .school-name {
    position: absolute;
    left: 62px;
    top: 50px;
    width: 300px;
    font-family: "Lora", Georgia, serif;
    font-weight: 400;
    font-size: 34px;
    line-height: 1.08;
    color: var(--navy);
    text-align: center;
  }
  .tagline {
    position: absolute;
    left: 394px;
    top: 78px;
    font-family: "Lora", Georgia, serif;
    font-weight: 500;
    font-size: 24px;
    line-height: 29px;
    letter-spacing: 0.6px;
    color: var(--navy);
    text-transform: uppercase;
  }
  .photo-strip {
    height: 228px;
    background: var(--navy);
    padding: 13px 0 14px;
    display: flex;
  }
  .photo { height: 201px; }
  .photo-classroom { width: 234px; background: linear-gradient(160deg, var(--photo-classroom-2), var(--photo-classroom)); }
  .photo-portrait { width: 350px; background: linear-gradient(90deg, var(--photo-portrait-2), var(--photo-portrait) 50%, var(--photo-portrait-2)); }
  .photo-yoga { width: 346px; background: linear-gradient(180deg, var(--photo-yoga) 55%, var(--photo-yoga-2)); }
  .photo-family { width: 192px; background: linear-gradient(160deg, var(--photo-family-2), var(--photo-family)); }
</style>
</head>
<body>
  <section class="banner">
    <header class="banner-header">
      <div class="school-name">The Linden School at Marwick</div>
      <p class="tagline">A caring community where students<br>with complex learning challenges<br>love to learn</p>
    </header>
    <div class="photo-strip">
      <div class="photo photo-classroom" role="img" aria-label="Teacher helping young students working on laptops in a classroom"></div>
      <div class="photo photo-portrait" role="img" aria-label="Smiling boy in a cap with hands on his head among classmates"></div>
      <div class="photo photo-yoga" role="img" aria-label="Students doing yoga side planks on mats in the school library"></div>
      <div class="photo photo-family" role="img" aria-label="Young girl with a parent and children outdoors at school"></div>
    </div>
  </section>
</body>
</html>
```